Driver License Monitoring Application Marketing Website

We need a new web design for our web application. The product is called "PermitPulseNow." We provide a driver license monitoring service to companies and local government bodies with driver fleets. Our current website is available at www.permitpulsenow.example.

I prefer a clean, single-page design with good SEO. Attached are some PDFs with data about the project.

Target Market(s)

Companies with driver fleets, local government.

Industry/Entity Type

Government

Coding

Coded - Design and coding required

Number of Pages Required

1 page

Colors
000000

Requirements
Must have
• Content from current www.permitpulsenow.example and attached PDFs.
Nice to have
• Prefer a simple Bootstrap or similar design for easy editing.
• Room for a simple video explanation of how the product works (we don't have an actual video yet)

```html
<!DOCTYPE html>
<html lang="en">
<head>
<meta charset="utf-8">
<title>PermitPulseNow – Florida Driver License Monitoring</title>
<link rel="stylesheet" href="https://fonts.googleapis.com/css2?family=Lato:wght@300;400;700;900&display=swap">
<style>
:root{
  --red:#c8161d;
  --red-dark:#a50f15;
  --red-soft:#e06366;
  --ink:#222222;
  --text:#444444;
  --muted:#777777;
  --green:#2a9a1f;
  --amber:#eea600;
  --ring:#eeeeee;
  --bracket:#c4c4c4;
  --footer:#2c2d30;
  --footer-bottom:#222326;
  --white:#ffffff;
}
*{box-sizing:border-box;margin:0;padding:0}
html,body{width:1200px;height:2699px;overflow:hidden}
body{position:relative;background:var(--white);font-family:'Lato',sans-serif;color:var(--text)}
.abs{position:absolute}

.top-rule{left:86px;top:0;width:1025px;height:3px;background:var(--red)}
.brand{left:105px;top:30px;font-weight:900;font-size:32px;color:var(--ink);letter-spacing:.5px}
.top-contact{left:882px;top:30px;font-size:13px;font-weight:700;color:var(--ink);line-height:20px}
.top-contact span{color:var(--red);margin-right:8px}

.hero{left:0;top:131px;width:1200px;height:774px;background:linear-gradient(120deg,#6f7880 0%,#a9b3b0 35%,#7fa552 60%,#4e7d2e 100%)}
.main-nav{left:86px;top:94px;width:1025px;height:68px;background:var(--red);display:flex;box-shadow:0 4px 8px rgba(0,0,0,.25)}
.main-nav a{color:var(--white);text-decoration:none;font-size:14px;font-weight:700;display:flex;align-items:center;justify-content:center;border-right:1px solid rgba(0,0,0,.18);height:100%}
.main-nav .search{flex:1;justify-content:space-between;padding:0 30px;font-weight:400;color:rgba(255,255,255,.65);border-right:none}
.headline{right:98px;top:262px;text-align:right}
.headline p{display:inline-block;background:rgba(30,30,30,.82);color:var(--white);font-size:48px;line-height:62px;padding:0 16px;margin-bottom:6px}
.headline em{color:var(--red);font-style:normal}

.title-band{left:0;top:905px;width:1200px;height:108px;background:linear-gradient(var(--red),var(--red-dark))}
.title-band h1{position:absolute;left:270px;top:24px;font-weight:300;font-size:46px;color:var(--white)}
.info-band{left:0;top:1013px;width:1200px;height:90px;background:#050505}
.info-band p{position:absolute;left:273px;top:24px;color:var(--white);font-size:16px;line-height:22px}
.info-band em{color:var(--red);font-style:normal}
.more-btn{left:918px;top:1030px;width:180px;height:61px;background:var(--red);color:var(--white);text-align:center;padding-top:10px}
.more-btn b{display:block;font-size:16px}
.more-btn small{font-size:12px;font-weight:700}
.state-map{left:86px;top:936px;width:160px;height:140px;background:linear-gradient(180deg,#f2c5c6,#c9c9c9)}

.monitoring{left:0;top:1150px;width:1200px;text-align:center}
.monitoring h2{font-weight:300;font-size:36px;color:var(--red)}
.monitoring h3{font-size:17px;font-weight:700;color:var(--ink);margin-top:8px}
.monitoring p{width:850px;margin:18px auto 0;font-size:14px;line-height:20px}
.stat{width:280px;text-align:center}
.stat svg{display:block;margin:0 auto}
.stat .num{position:absolute;top:52px;left:0;width:280px;font-size:36px;font-weight:300;color:var(--text)}
.stat .unit{position:absolute;top:95px;left:0;width:280px;font-size:16px;color:var(--text)}
.stat .caption{margin-top:24px;height:54px;display:flex;align-items:center;justify-content:center;font-size:18px;line-height:22px;
  border-left:2px solid var(--bracket);border-right:2px solid var(--bracket);
  background:
    linear-gradient(var(--bracket),var(--bracket)) left top/8px 2px no-repeat,
    linear-gradient(var(--bracket),var(--bracket)) left bottom/8px 2px no-repeat,
    linear-gradient(var(--bracket),var(--bracket)) right top/8px 2px no-repeat,
    linear-gradient(var(--bracket),var(--bracket)) right bottom/8px 2px no-repeat}
.stat .caption b{font-weight:700}
.stat .caption b.g{color:var(--green)}
.stat .caption b.a{color:var(--amber)}
.stat .caption b.r{color:var(--red)}

.services{left:0;top:1685px;width:1200px;height:394px;background:linear-gradient(90deg,var(--red-soft),#d8494d 50%,var(--red-soft))}
.card{top:1732px;width:222px;height:208px;background:var(--white);text-align:center;box-shadow:0 2px 6px rgba(0,0,0,.2)}
.card .thumb{height:109px}
.card h4{font-weight:400;font-size:25px;color:var(--red);margin-top:14px}
.card span{font-size:19px;color:var(--text)}
.cta{left:97px;top:2020px;width:1006px;height:79px;background:linear-gradient(var(--red),var(--red-dark));color:var(--white);font-weight:700;font-size:35px;display:flex;align-items:center;justify-content:center;box-shadow:0 4px 8px rgba(0,0,0,.3)}

.alerts{left:0;top:2145px;width:1200px;text-align:center}
.alerts h2{font-weight:300;font-size:36px;color:var(--red);margin-bottom:22px}
.tag-row{display:flex;justify-content:center;gap:8px;margin-bottom:5px}
.tag{border:1px solid #cfcfcf;font-size:20px;color:var(--ink);padding:2px 8px;line-height:24px}

.footer{left:0;top:2462px;width:1200px;height:184px;background:var(--footer)}
.footer-rule{left:86px;top:2462px;width:1025px;height:4px;background:var(--red)}
.foot-brand{left:92px;top:2488px;font-weight:900;font-size:25px;color:var(--white)}
.foot-address{left:92px;top:2530px;font-size:13px;line-height:16px;color:var(--white)}
.foot-col{top:2500px;font-size:13px;line-height:21px;color:#bdbdbd}
.foot-col h5{font-size:13px;font-weight:700;color:var(--white);margin-bottom:10px}
.foot-col .active{color:var(--red)}
.foot-map{left:864px;top:2490px;width:220px;height:130px;background:linear-gradient(180deg,var(--red),var(--red-dark))}
.foot-map-text{left:887px;top:2526px;font-weight:300;font-size:25px;line-height:27px;color:var(--white)}
.foot-bottom{left:0;top:2646px;width:1200px;height:53px;background:var(--footer-bottom);font-size:12px;color:#7a7a7a}
.foot-bottom .copy{position:absolute;left:92px;top:20px}
.foot-bottom .privacy{position:absolute;left:1013px;top:20px}
.social{position:absolute;left:560px;top:20px;display:flex;gap:30px}
.social i{display:block;width:12px;height:12px;border-radius:50%;background:var(--red)}
</style>
</head>
<body>

<div class="abs top-rule"></div>
<div class="abs brand">PermitPulseNow</div>
<div class="abs top-contact">
  <div><span>&#9990;</span>1.555.010.4827</div>
  <div><span>&#9993;</span>contact@permitpulsenow.example</div>
</div>

<div class="abs hero" role="img" aria-label="Photo of a truck driver at the wheel of his cab, green forest outside the window"></div>
<nav class="abs main-nav">
  <a href="#" style="width:118px">HOME</a>
  <a href="#" style="width:185px">LICENSE MONITORING</a>
  <a href="#" style="width:135px">ABOUT US</a>
  <a href="#" style="width:132px">CONTACT</a>
  <a href="#" style="width:170px">CLIENT LOGIN</a>
  <a href="#" class="search">SEARCH
    <svg width="16" height="16" viewBox="0 0 16 16"><circle cx="6.5" cy="6.5" r="5" fill="none" stroke="#fff" stroke-width="2"/><line x1="10.5" y1="10.5" x2="15" y2="15" stroke="#fff" stroke-width="2"/></svg>
  </a>
</nav>
<div class="abs headline">
  <p>How many of your drivers</p><br>
  <p>currently have a</p><br>
  <p><em>suspended</em> license?</p>
</div>

<div class="abs title-band"><h1>Florida Driver License Monitoring</h1></div>
<div class="abs info-band">
  <p>Monitor your fleet <em>electronically</em>. Get alerts by <em>email</em> and <em>online</em>.<br>Never let another unlicensed or unauthorized driver behind the wheel</p>
</div>
<div class="abs state-map" role="img" aria-label="Map of the state of Florida"></div>
<a class="abs more-btn"><b>MORE INFO &nbsp;›</b><small>TRACK YOUR FLEET</small></a>

<section class="abs monitoring">
  <h2>License Monitoring</h2>
  <h3>Monitor your drivers electronically, twenty-four hours a day.</h3>
  <p>How many of your drivers currently have a suspended license? The answer may surprise you. Driving with a suspended license is the most commonly committed offense in America. In 2011, over 1.8 million licenses got suspended in Florida. With just over 15 million drivers, that's 12% of all licensed Florida drivers.</p>
</section>

<div class="abs stat" style="left:143px;top:1355px">
  <svg width="170" height="170" viewBox="0 0 170 170"><circle cx="85" cy="85" r="77" fill="none" stroke="var(--ring)" stroke-width="16"/><circle cx="85" cy="85" r="77" fill="none" stroke="var(--green)" stroke-width="16" stroke-dasharray="266 484" transform="rotate(-90 85 85)"/></svg>
  <div class="num">15</div><div class="unit">MILLION</div>
  <div class="caption"><span>Florida has<br><b class="g">15 million</b> drivers</span></div>
</div>
<div class="abs stat" style="left:461px;top:1355px">
  <svg width="170" height="170" viewBox="0 0 170 170"><circle cx="85" cy="85" r="77" fill="none" stroke="var(--ring)" stroke-width="16"/><circle cx="85" cy="85" r="77" fill="none" stroke="var(--amber)" stroke-width="16" stroke-dasharray="58 484" transform="rotate(-90 85 85)"/></svg>
  <div class="num">1.8</div><div class="unit">MILLION</div>
  <div class="caption"><span>Approximately <b class="a">1.8 million</b><br>suspended yearly</span></div>
</div>
<div class="abs stat" style="left:780px;top:1355px">
  <svg width="170" height="170" viewBox="0 0 170 170"><circle cx="85" cy="85" r="77" fill="none" stroke="var(--ring)" stroke-width="16"/><circle cx="85" cy="85" r="77" fill="none" stroke="var(--red)" stroke-width="16" stroke-dasharray="105 484" transform="rotate(-90 85 85)"/></svg>
  <div class="num">12%</div><div class="unit">EXTRA</div>
  <div class="caption"><span>Which is <b class="r">12%</b>, etc.</span></div>
</div>

<div class="abs services" role="img" aria-label="Faded red-tinted photo of a driver in a cab"></div>
<div class="abs card" style="left:88px"><div class="thumb" role="img" aria-label="Photo of a smiling driver in a truck" style="background:linear-gradient(#7a7f84,#c8c2b8)"></div><h4>What We Do</h4><span>License Monitoring</span></div>
<div class="abs card" style="left:356px"><div class="thumb" role="img" aria-label="Photo of a blue semi truck with white trailer" style="background:linear-gradient(#9fc3e3,#3e5f8c)"></div><h4>Commercial</h4><span>Private Sector</span></div>
<div class="abs card" style="left:623px"><div class="thumb" role="img" aria-label="Photo representing state government" style="background:linear-gradient(#eedcdc,#d98a8c)"></div><h4>Government</h4><span>Public Sector</span></div>
<div class="abs card" style="left:889px"><div class="thumb" role="img" aria-label="Photo of a driver giving a thumbs up behind a map" style="background:linear-gradient(#a7b2bd,#d9d2c4)"></div><h4>About Us</h4><span>Florida Law Authorities</span></div>
<a class="abs cta">CONTACT US FOR A PRODUCT DEMONSTRATION &nbsp;›</a>

<section class="abs alerts">
  <h2>Get Instant Alert for</h2>
  <div class="tag-row"><span class="tag">Suspensions for Child Support</span><span class="tag">Suspensions for Unpaid Fines</span><span class="tag">Suspensions for Court Obligations</span></div>
  <div class="tag-row"><span class="tag">Revocations for Accidents</span><span class="tag">Revocations for Convictions</span></div>
  <div class="tag-row"><span class="tag">Commercial Vehicle Desqualifications</span><span class="tag">Medical Certificate Expirations</span></div>
  <div class="tag-row"><span class="tag">License Expirations</span><span class="tag">License Cancellations</span></div>
  <div class="tag-row"><span class="tag">All Other License Sanctions</span></div>
</section>

<footer class="abs footer"></footer>
<div class="abs footer-rule"></div>
<div class="abs foot-brand">PermitPulseNow</div>
<div class="abs foot-address">PermitPulseNow, Inc.<br>4120 Harbor Point Rd., Ste 210<br>Coral Bay, FL 33099<br>T 1.555.010.4827<br>F 1.555.010.4830<br>contact@permitpulsenow.example</div>
<div class="abs foot-col" style="left:486px"><h5>NAVIGATIONS</h5><div class="active">Home</div><div>License Monitoring</div><div>About Us</div><div>Contact</div><div>Client Login</div></div>
<div class="abs foot-col" style="left:664px"><h5>OUR SERVICES FOR</h5><div>Commercial</div><div>Government</div></div>
<div class="abs foot-map" role="img" aria-label="Map of the state of Florida"></div>
<div class="abs foot-map-text">FLORIDA<br>DRIVER LICENSE<br>MONITORING</div>
<div class="abs foot-bottom">
  <span class="copy">Copyright © 2015 PermitPulseNow.example</span>
  <div class="social"><i></i><i></i><i></i></div>
  <span class="privacy">Privacy Policy</span>
</div>

</body>
</html>
```